Personal Blog

The wordpress blog style and layout should be similar to http://www.ninalofwent.com

homepage: my photo, list of things, call to action then 3 boxes (The Blog, The Book and podcast)

Other pages: About us, Blog, Consulting, Contact

Target Market(s)

Web Marketing Consultant

Industry/Entity Type

Consulting

Colors
3277b5
33a6d7
f04a50
f68e4e
33b7a4

```html
<!DOCTYPE html>
<html lang="en">
<head>
<meta charset="utf-8">
<title>Marek Talvani – Personal Blog</title>
<link rel="stylesheet" href="https://fonts.googleapis.com/css2?family=Dosis:wght@500;600;700&family=Open+Sans:wght@400;600&family=Roboto+Condensed:wght@700&display=swap">
<style>
  :root{
    --teal:#2ec6b2;
    --teal-dark:#1fa898;
    --ink:#1d2b2c;
    --text:#333b3c;
    --grey-icon:#6f6f6f;
    --panel:#eef4f5;
    --line:#d5dcdd;
    --footer:#0f2527;
    --footer-text:#e8efef;
    --white:#ffffff;
  }
  *{box-sizing:border-box;margin:0;padding:0}
  html,body{width:1200px;height:2200px;overflow:hidden}
  body{background:var(--panel);font-family:"Open Sans",Arial,sans-serif;color:var(--text);position:relative}

  /* Header */
  .site-header{height:134px;background:linear-gradient(90deg,#3cc7b4 0%,#79ddd0 45%,#a9ece3 100%);position:relative}
  .brand{position:absolute;left:46px;top:26px;display:flex;align-items:center;height:72px}
  .brand-first{background:#1e3536;color:var(--white);font:700 44px/72px "Dosis",sans-serif;padding:0 26px;border-radius:6px}
  .brand-last{color:var(--white);font:700 44px/72px "Dosis",sans-serif;padding-left:14px}
  .main-nav{position:absolute;right:46px;top:50px;display:flex;gap:26px}
  .main-nav a{font:700 22px/1 "Roboto Condensed",sans-serif;color:var(--ink);text-decoration:none}

  /* Hero */
  .hero{height:416px;background:linear-gradient(180deg,#f4fbfb 0%,#e7f1f2 100%);position:relative;border-bottom:1px solid var(--line)}
  .hero-title{position:absolute;left:58px;top:34px;width:1100px;font:600 42px/1.24 "Dosis",sans-serif;color:var(--teal)}
  .hero-title strong{color:var(--ink);font-weight:600}
  .topic-list{position:absolute;left:58px;top:158px;list-style:none}
  .topic-list li{font:400 21px/41px "Open Sans",sans-serif;color:var(--ink);padding-left:22px;position:relative}
  .topic-list li::before{content:"›";position:absolute;left:0;top:-1px;color:var(--teal);font-weight:700;font-size:24px}
  .hero-photo{position:absolute;left:618px;top:200px;width:530px;height:216px;border-radius:4px 4px 0 0;background:linear-gradient(135deg,#dfe7ea 0%,#c9d6da 45%,#f3f6f7 100%)}

  /* Testimonial */
  .testimonial{height:183px;position:relative;text-align:center}
  .quote-mark{position:absolute;left:578px;top:30px;width:44px;height:34px}
  .testimonial blockquote{position:absolute;left:60px;right:60px;top:88px;font:400 23px/1.4 "Open Sans",sans-serif;color:var(--text)}
  .testimonial cite{position:absolute;right:100px;top:156px;font:italic 400 17px/1 "Open Sans",sans-serif;color:var(--teal-dark)}

  /* Feature boxes */
  .features{position:absolute;left:46px;top:765px;width:1107px;display:flex;gap:23px}
  .feature{width:354px;height:378px;background:var(--white);border:2px solid var(--line);border-radius:3px;position:relative;text-align:center}
  .feature-icon{position:absolute;left:102px;top:36px;width:150px;height:150px}
  .feature h2{position:absolute;left:0;right:0;top:198px;font:700 32px/1 "Dosis",sans-serif;color:var(--grey-icon)}
  .feature.is-active h2{color:var(--teal)}
  .feature p{position:absolute;left:24px;right:24px;top:242px;font:400 14.5px/1.5 "Open Sans",sans-serif;color:var(--ink)}
  .pill{display:inline-block;position:relative;height:26px;padding:0 30px 0 16px;border-radius:13px;background:#e3e6e6;border:1px solid #b9c0c1;font:600 14px/24px "Open Sans",sans-serif;color:var(--ink);white-space:nowrap}
  .pill::after{content:"›";position:absolute;right:9px;top:0;width:14px;height:14px;border:1px solid currentColor;border-radius:50%;font-size:13px;line-height:12px;margin-top:5px;text-align:center}
  .feature .pill{position:absolute;left:50%;transform:translateX(-50%);top:362px}
  .feature.is-active .pill{background:var(--teal);border-color:var(--teal);color:var(--white)}

  /* Recent posts */
  .section-rule{position:absolute;left:46px;top:1220px;width:1107px;height:2px;background:var(--line)}
  .section-title{position:absolute;left:0;right:0;top:1200px;text-align:center}
  .section-title span{display:inline-block;background:var(--panel);padding:0 24px;font:700 32px/42px "Roboto Condensed",sans-serif;color:var(--ink)}
  .posts{position:absolute;left:46px;top:1283px;width:1107px;display:flex;gap:26px}
  .post{width:257px;height:460px;background:var(--white);border:2px solid var(--line);display:flex;flex-direction:column;padding:6px 6px 22px}
  .post.is-active{border-color:var(--teal)}
  .post-image{flex:0 0 186px}
  .post h3{margin:22px 8px 0 14px;font:600 21px/1.2 "Dosis",sans-serif;color:#8a8f90}
  .post.is-active h3{color:var(--teal)}
  .post p{margin:10px 8px 0 14px;font:400 13.5px/1.55 "Open Sans",sans-serif;color:var(--ink)}
  .post .pill{margin:auto 0 0 14px;align-self:flex-start;background:var(--white);border-color:var(--ink)}
  .post.is-active .pill{background:var(--teal);border-color:var(--teal);color:var(--white)}

  /* Footer */
  .site-footer{position:absolute;left:0;top:1838px;width:1200px;height:362px;background:var(--footer);color:var(--footer-text);border-top:6px solid #d7dedf}
  .footer-col{position:absolute;top:42px}
  .footer-col h4{font:700 29px/1 "Roboto Condensed",sans-serif;color:var(--white);margin-bottom:20px}
  .about-col{left:46px;width:330px}
  .about-col p{font:400 14.5px/1.5 "Open Sans",sans-serif;margin-bottom:8px}
  .about-col a{font:400 14.5px/1.5 "Open Sans",sans-serif;color:var(--teal)}
  .signup-col{left:421px;width:340px}
  .field{display:block;width:338px;height:42px;border-radius:4px;background:var(--white);margin-bottom:12px;padding:0 12px;font:400 15px/42px "Open Sans",sans-serif;color:#444}
  .join{display:block;width:338px;height:50px;margin-top:12px;border-radius:4px;background:var(--teal);color:var(--white);font:700 27px/50px "Roboto Condensed",sans-serif;text-align:center}
  .connect-col{left:800px;width:320px}
  .social{display:flex;gap:16px}
  .social span{width:56px;height:56px;border-radius:4px;background:#8d9596;color:var(--footer);font:700 11px/56px "Open Sans",sans-serif;text-align:center}
  .social span.is-active{background:var(--teal)}
  .connect-col p{width:280px;text-align:center;font:400 14.5px/1.5 "Open Sans",sans-serif;margin-top:14px}
  .connect-col p a{color:var(--teal)}
  .copyright{position:absolute;left:0;right:0;top:318px;text-align:center;font:400 15px/1 "Open Sans",sans-serif}
  .copyright a{color:var(--teal)}
</style>
</head>
<body>

<header class="site-header">
  <div class="brand"><span class="brand-first">Marek</span><span class="brand-last">Talvani</span></div>
  <nav class="main-nav">
    <a href="#">ABOUT</a><a href="#">BLOG</a><a href="#">CONSULTING</a><a href="#">RESOURCES</a><a href="#">BOOK</a><a href="#">CONTACT</a>
  </nav>
</header>

<section class="hero">
  <h1 class="hero-title">Test go here and <strong>Product Management</strong>, text here <strong>Online Marketing</strong>,<br>to learn these topics:</h1>
  <ul class="topic-list">
    <li>Product Management</li>
    <li>Customer Development</li>
    <li>Digital Marketing</li>
    <li>Branding &amp; Reputation</li>
    <li>Entrepreneurship</li>
  </ul>
  <div class="hero-photo" role="img" aria-label="Portrait of the author at a desk beside a computer monitor"></div>
</section>

<section class="testimonial">
  <svg class="quote-mark" viewBox="0 0 44 34" aria-hidden="true"><path d="M2 34V18C2 8 8 2 18 0v6c-5 2-7 5-7 10h7v18zM26 34V18c0-10 6-16 16-18v6c-5 2-7 5-7 10h7v18z" fill="#c9d2d3"/></svg>
  <blockquote>“... I was blown away by his breadth of industry knowledge, the straight talking delivery and collaborative format. A highly recommended social media expert and thought leader...”</blockquote>
  <cite>-Lena Corvath - Marketing</cite>
</section>

<div class="features">
  <article class="feature is-active">
    <svg class="feature-icon" viewBox="0 0 150 150" aria-hidden="true">
      <circle cx="75" cy="75" r="73" fill="none" stroke="#cfd6d7" stroke-width="3"/>
      <circle cx="75" cy="75" r="64" fill="var(--teal)"/>
      <path d="M48 58c0-10 10-17 24-17s24 7 24 17-10 17-24 17c-3 0-5 0-8-1l-12 7 3-10c-5-3-7-8-7-13z" fill="none" stroke="#fff" stroke-width="5" stroke-linejoin="round"/>
      <path d="M78 82c13 0 24-6 25-15 6 3 9 8 9 13 0 5-2 9-6 12l2 9-10-6c-3 1-6 1-9 1-10 0-18-4-22-10" fill="none" stroke="#fff" stroke-width="5" stroke-linejoin="round"/>
    </svg>
    <h2>The Blog</h2>
    <p>Lorem Ipsum is simply dummy text of the printing &amp; typesetting industry. Lorem Ipsum has been industry's standard dummy text ever since the 15000s.</p>
    <span class="pill">Read More</span>
  </article>
  <article class="feature">
    <svg class="feature-icon" viewBox="0 0 150 150" aria-hidden="true">
      <circle cx="75" cy="75" r="73" fill="none" stroke="#cfd6d7" stroke-width="3"/>
      <circle cx="75" cy="75" r="64" fill="var(--grey-icon)"/>
      <rect x="52" y="40" width="48" height="66" rx="4" fill="none" stroke="#fff" stroke-width="5"/>
      <line x1="60" y1="40" x2="60" y2="106" stroke="#fff" stroke-width="4"/>
      <line x1="68" y1="56" x2="92" y2="56" stroke="#fff" stroke-width="4"/>
    </svg>
    <h2>The Book</h2>
    <p>Lorem Ipsum is simply dummy text of the printing &amp; typesetting industry. Lorem Ipsum has been industry's standard dummy text ever since the 15000s.</p>
    <span class="pill">Read More</span>
  </article>
  <article class="feature">
    <svg class="feature-icon" viewBox="0 0 150 150" aria-hidden="true">
      <circle cx="75" cy="75" r="73" fill="none" stroke="#cfd6d7" stroke-width="3"/>
      <circle cx="75" cy="75" r="64" fill="var(--grey-icon)"/>
      <circle cx="66" cy="60" r="13" fill="#fff"/>
      <path d="M42 102c0-16 10-25 24-25s24 9 24 25z" fill="#fff"/>
      <circle cx="90" cy="56" r="10" fill="#fff" opacity=".8"/>
      <path d="M94 70c10 2 16 10 16 24H95c0-9-3-16-9-20z" fill="#fff" opacity=".8"/>
    </svg>
    <h2>Consulting</h2>
    <p>Lorem Ipsum is simply dummy text of the printing &amp; typesetting industry. Lorem Ipsum has been industry's standard dummy text ever since the 15000s.</p>
    <span class="pill">Read More</span>
  </article>
</div>

<div class="section-rule"></div>
<h2 class="section-title"><span>RECENT POSTS</span></h2>

<div class="posts">
  <article class="post is-active">
    <div class="post-image" role="img" aria-label="Team meeting around a table with laptops" style="background:linear-gradient(135deg,#9a6a3f,#d8cfc2 60%,#6d5a48)"></div>
    <h3>Yet Another Video Post Format With Embedded Media</h3>
    <p>Lorem Ipsum is simply dummy text of the printing &amp; typesetting industry. Lorem Ipsum has ...</p>
    <span class="pill">Read More</span>
  </article>
  <article class="post">
    <div class="post-image" role="img" aria-label="Group of business people in suits" style="background:linear-gradient(135deg,#e9ecee,#4a4f57 55%,#c8ccd0)"></div>
    <h3>Yet Another Video Post Format With Embedded Media</h3>
    <p>Lorem Ipsum is simply dummy text of the printing &amp; typesetting industry. Lorem Ipsum has ...</p>
    <span class="pill">Read More</span>
  </article>
  <article class="post">
    <div class="post-image" role="img" aria-label="Hand touching a virtual screen interface" style="background:linear-gradient(135deg,#3b4046,#a3a9b0 50%,#2b2f34)"></div>
    <h3>Yet Another Video Post Format With Embedded Media</h3>
    <p>Lorem Ipsum is simply dummy text of the printing &amp; typesetting industry. Lorem Ipsum has ...</p>
    <span class="pill">Read More</span>
  </article>
  <article class="post">
    <div class="post-image" role="img" aria-label="Hands typing on a keyboard" style="background:linear-gradient(135deg,#f2f2f2,#5b5e63 60%,#cfd1d3)"></div>
    <h3>Yet Another Video Post Format With Embedded Media</h3>
    <p>Lorem Ipsum is simply dummy text of the printing &amp; typesetting industry. Lorem Ipsum has ...</p>
    <span class="pill">Read More</span>
  </article>
</div>

<footer class="site-footer">
  <div class="footer-col about-col">
    <h4>ENTREPRENEUR, SPEAKER,</h4>
    <p>Lorem Ipsum is simply dummy text of the printing &amp; typesetting industry. Lorem Ipsum has been industry's standard dummy text ever since the 15000s.</p>
    <p>Lorem Ipsum is simply dummy text of the printing &amp; typesetting industry.</p>
    <a href="#">[ Read the long-winded version! ]</a>
  </div>
  <div class="footer-col signup-col">
    <h4>JOIN MY NEW BUSINESS</h4>
    <span class="field">Enter your name...</span>
    <span class="field">Enter your email...</span>
    <span class="join">JOIN FOR FREE!</span>
  </div>
  <div class="footer-col connect-col">
    <h4>CONNECT WITH ME</h4>
    <div class="social">
      <span class="is-active">Friendo</span><span>Chirp</span><span>Feed</span><span>Clipcast</span>
    </div>
    <p>OR<br>Connect with via <a href="#">email</a></p>
  </div>
  <p class="copyright">© 2014 M. Talvani <a href="#">www.marektalvani.com</a> | All Right Reserved.</p>
</footer>

</body>
</html>
```